Brookvale Animal Hospital brochure

We have found that our current clients do not know all of the services that we offer so we want to make a hospital brochure to make our services more known. Our website has all of our services listed but we find that clients aren't looking at our website as much as we would like so we are hoping a hospital brochure can sum up our main services and maybe lead to more people visiting our website. Our hospital colors are blue and maroon and our moto is "Outstanding Medicine, Extraordinary Service." Some of the service we would like to promote more include digital x-ray, ultrasounds, echocardiograms, laser therapy and dentals. We also offer after hours emergency care but only to our current clients. You can find more services listed on our website We are in a small town so we want a personal yet professional feel.

Feel free to visit our website to get a better feel for our business https://thebrookvalepets.example/

Industry/Entity Type

Veterinary

Requirements
Must have
• 6-8 panel brochure
Nice to have
• I included some photos from around the hospital. If you feel that you can make a few work in the brochure then great but don't feel obligated to.

```html
<!DOCTYPE html>
<html lang="en">
<head>
<meta charset="utf-8">
<title>Brookvale Animal Hospital Trifold Brochure</title>
<link rel="stylesheet" href="https://fonts.googleapis.com/css2?family=EB+Garamond:wght@400;500;600&display=swap">
<style>
:root{
  --backdrop:#9cc6d6;
  --maroon:#8f1620;
  --gold:#b48c4e;
  --taupe:#a99388;
  --cream:#fbf4ec;
  --fold:#6e0e16;
}
*{margin:0;padding:0;box-sizing:border-box}
html,body{width:1200px;height:478px;overflow:hidden;background:var(--backdrop)}
body{font-family:"EB Garamond",Georgia,serif;color:var(--cream);position:relative}

.sheet{position:absolute;top:40px;height:398px;background:var(--maroon);box-shadow:0 6px 14px rgba(0,0,0,.18);overflow:hidden}
.outer-sheet{left:18px;width:555px}
.inner-sheet{left:608px;width:573px}
.panel{position:absolute;top:0;height:398px;overflow:hidden}
.outer-sheet .panel{width:185px}
.inner-sheet .panel{width:191px}
.fold{position:absolute;top:0;width:1px;height:100%;background:var(--fold);z-index:3}
.abs{position:absolute}
.deco{position:absolute;left:0;top:0}

.headline{color:var(--gold);font-weight:400;line-height:1.05}
.body-copy{font-size:9px;line-height:1.18}

/* testimonials panel */
.bark-title{left:14px;top:18px;font-size:24px;line-height:.95;color:var(--gold);font-weight:500}
.testimonial{left:72px;width:104px;font-size:7px;line-height:1.25;text-align:center}
.testimonial .who{display:block;margin-top:4px;text-align:right}

/* mailing panel */
.address{left:16px;top:288px;font-size:7.5px;line-height:1.35}
.back-logo{left:16px;top:352px;display:flex;align-items:center;gap:6px;font-size:7.5px}
.badge{width:18px;height:14px;background:var(--cream);opacity:.85}

/* front cover */
.cover-title{left:16px;top:26px;font-size:26px;line-height:.92;color:var(--gold);font-weight:600}
.species{right:12px;top:226px;width:110px;text-align:right;font-size:7px;line-height:1.25}
.cover-logo{right:10px;top:318px;width:76px;text-align:center}
.cover-logo .mark{display:flex;align-items:center;gap:5px;font-size:8.5px;line-height:1.1;text-align:left;color:var(--cream)}
.cover-logo .dot{flex:none;width:11px;height:11px;border-radius:50%;background:var(--cream)}
.motto{margin-top:6px;font-size:7px;line-height:1.2;color:var(--maroon)}

/* services */
.service-col{position:absolute;width:80px;font-size:8px;line-height:1.12}
.service-col p{margin-bottom:9px}
.service-col .note{font-size:5.8px;line-height:1.2;color:var(--gold);margin-top:-5px}
.photo-circle{position:absolute;top:20px;width:52px;height:52px;border-radius:50%;border:2px solid var(--cream)}
</style>
</head>
<body>

<!-- Outer side: three panels -->
<div class="sheet outer-sheet" aria-label="Outer side">

  <section class="panel" style="left:0" aria-label="Testimonials panel">
    <svg class="deco" width="185" height="398"><path d="M0 398 L0 310 Q 90 325 185 292 L185 398 Z" fill="var(--taupe)"/></svg>
    <h2 class="abs bark-title">The<br>Bark<br>of<br>The<br>Town</h2>
    <p class="abs testimonial" style="top:20px">“Can't say enough fantastic things about this place. Just superb. Dr. Pryor and Dr. Hale have been absolutely terrific with my kitty, who was a nervous wreck when she first came. Such kindness and patience from the staff here, she calmed down so much! She got great treatment!”<span class="who">Marla</span></p>
    <p class="abs testimonial" style="top:148px">“Dr. Hale and her assistant are absolutely amazing! They treated my macaw Snowy with patience, compassion and understanding. They took the time to answer all my questions and concerns. I love the receptionist as well. This is truly an extraordinary place with extraordinary people. Thank you all so much. The price was very reasonable.”<span class="who">Tessa</span></p>
  </section>

  <section class="panel" style="left:185px" aria-label="Mailing panel">
    <svg class="deco" width="185" height="398">
      <path d="M0 398 L0 292 Q 95 262 185 250 L185 398 Z" fill="var(--taupe)"/>
      <circle cx="92" cy="160" r="72" fill="none" stroke="var(--gold)" stroke-width="1"/>
    </svg>
    <div class="abs" role="img" aria-label="Orange and white cat sitting" style="left:37px;top:110px;width:110px;height:150px;border-radius:55px 55px 0 0;background:radial-gradient(circle at 50% 40%,#e6dfd6,#c58d55 60%,#9a6b45)"></div>
    <p class="abs address">Brookvale Animal Hospital<br>412 Mill Creek Road<br>Brookvale, Vermont, 05999<br>https://thebrookvalepets.example/</p>
    <div class="abs back-logo"><span>Brookvale Animal Hospital</span><span class="badge"></span></div>
  </section>

  <section class="panel" style="left:370px" aria-label="Front cover">
    <svg class="deco" width="185" height="398">
      <path d="M0 398 L0 340 Q 95 305 185 285 L185 398 Z" fill="var(--taupe)"/>
      <circle cx="140" cy="165" r="50" fill="none" stroke="var(--gold)" stroke-width="1"/>
    </svg>
    <h1 class="abs cover-title">We Care<br>For Your<br>Love Ones</h1>
    <div class="abs" role="img" aria-label="Blue and gold macaw" style="left:105px;top:128px;width:80px;height:76px;border-radius:38px 0 0 38px;background:linear-gradient(160deg,#c7c0b4,#3f8bc1 55%,#e1b53a)"></div>
    <p class="abs species">We Care for Dogs, Cats, Birds, Small Mammals, And Other Exotic Pets.</p>
    <div class="abs" role="img" aria-label="Tan mastiff dog with tongue out" style="left:0;top:262px;width:92px;height:136px;border-radius:0 46px 0 0;background:linear-gradient(150deg,#c99a63,#a06c3d 60%,#6a4223)"></div>
    <div class="abs cover-logo">
      <div class="mark"><span class="dot"></span><span>Brookvale Animal Hospital</span></div>
      <p class="motto">Outstanding Medicine, Extraordinary Service</p>
    </div>
  </section>

  <div class="fold" style="left:185px"></div>
  <div class="fold" style="left:370px"></div>
</div>

<!-- Inner side: three panels -->
<div class="sheet inner-sheet" aria-label="Inner side">
  <svg class="deco" width="573" height="398" style="z-index:0">
    <path d="M382 398 Q 500 390 573 322 L573 398 Z" fill="var(--taupe)"/>
    <circle cx="191" cy="-8" r="62" fill="none" stroke="var(--gold)" stroke-width="1"/>
  </svg>

  <section class="panel" style="left:0" aria-label="Introduction panel">
    <h2 class="abs headline" style="left:16px;top:20px;font-size:20px">Your Pet Means<br>The World To You</h2>
    <p class="abs body-copy" style="left:16px;top:76px;width:160px">And because of that, you want to know that they are receiving the kind of medical care you would want for any member of your family.</p>
    <p class="abs body-copy" style="left:16px;top:134px;width:160px">The team of veterinary professionals here is truly top notch, and the technology at their.</p>
    <div class="abs" role="img" aria-label="Small rabbit silhouette" style="left:155px;top:178px;width:15px;height:19px;border-radius:45%;background:var(--gold)"></div>
    <p class="abs body-copy" style="left:16px;top:208px;width:160px;text-align:right">We built Brookvale Animal Hospital for you. It is so important to us that you can walk into an environment where you feel you are always put</p>
    <h2 class="abs headline" style="left:16px;top:296px;font-size:17px">Every Patient,<br>Every Time.<br>Our Complete<br>Care Services:</h2>
  </section>

  <section class="panel" style="left:191px" aria-label="Services panel">
    <div class="service-col" style="left:16px;top:28px;width:78px"><p>Allergy and Dermatology Testing</p><p>Avian Care</p><p>Blood Tests and Urine Screening</p><p>Cardiology Care</p><p>Canine and Feline Dental Care</p></div>
    <div class="service-col" style="left:100px;top:28px;width:78px"><p>Cold Laser Therapy</p><p class="note">Laser therapy is a drug-free, surgery-free and pain-free procedure that only takes minutes to perform.</p><p>Emergency Care</p><p>End-Of-Life Care</p><p>Digital X-Ray</p><p class="note">Our ClearView DR is a state-of-the-art digital x-ray unit that allows us to capture and interpret computerized digital x-rays quickly, more effectively, and with far greater detail than ever before.</p><p>Eye Care</p></div>
    <div class="abs" role="img" aria-label="Cockatoo silhouette" style="left:16px;top:330px;width:18px;height:42px;border-radius:50% 50% 30% 30%;background:var(--gold)"></div>
  </section>

  <section class="panel" style="left:382px" aria-label="More services panel">
    <div class="photo-circle" role="img" aria-label="Technician examining a pet on a table" style="left:14px;background:linear-gradient(140deg,#9aa38f,#2f3f6e 60%,#d8d2c8)"></div>
    <div class="photo-circle" role="img" aria-label="Veterinary surgeon in scrubs during a procedure" style="left:70px;background:linear-gradient(140deg,#8cb6a8,#3d6f7f 55%,#d9d6cf)"></div>
    <div class="photo-circle" role="img" aria-label="Vet performing an ultrasound on a cat" style="left:126px;background:linear-gradient(140deg,#ece8e2,#c7c2bb 50%,#24304f)"></div>
    <div class="service-col" style="left:16px;top:90px;width:78px"><p>Exotic Pet Care</p><p>Flea and Tick Prevention</p><p>Heartwor Preventative</p><p>House Calls</p><p>In-House Laboratory</p><p>Microchipping</p><p>Nutritional Consultations</p></div>
    <div class="service-col" style="left:100px;top:90px;width:80px"><p>Orthopedic Surgery</p><p>Parasite Testing and Treatment</p><p>Puppy and Kitten Care</p><p>Senior Wellness</p><p>Soft Tissue Surgery</p><p>Ultrasound</p><p>Vaccinations</p><p>Wellness Exams</p></div>
    <h2 class="abs headline" style="left:16px;top:300px;font-size:14px;line-height:1">The Care You Would<br>Want For Any<br>Member Of Your<br>Family.</h2>
    <div class="abs" role="img" aria-label="Giant tortoise" style="left:128px;top:340px;width:63px;height:58px;border-radius:60% 0 0 0;background:linear-gradient(150deg,#8a7a5c,#5b4a33 55%,#3b2f20)"></div>
  </section>

  <div class="fold" style="left:191px"></div>
  <div class="fold" style="left:382px"></div>
</div>

</body>
</html>
```